RIVERSTONE PAVING & EARTHWORKS

I would like the front of the card to have my logo centred.
I need it to have my contact details on the back of the card which are: RiverstonePavingEarthworks@mailbrook.net
0439268417
and a Facebook icon

```html
<!DOCTYPE html>
<html lang="en">
<head>
<meta charset="utf-8">
<title>Riverstone Paving &amp; Earthworks — Business Card</title>
<link href="https://fonts.googleapis.com/css2?family=Noto+Sans:wght@400&family=Saira+Condensed:wght@800&display=swap" rel="stylesheet">
<style>
  :root {
    --page-bg: #f8f8f8;
    --card-white: #ffffff;
    --navy: #003075;
    --light-grey: #cccccc;
  }
  * { box-sizing: border-box; margin: 0; padding: 0; }
  html, body {
    width: 1200px;
    height: 1200px;
    overflow: hidden;
    background: var(--page-bg);
  }
  .canvas {
    position: relative;
    width: 1200px;
    height: 1200px;
  }
  .card {
    position: absolute;
    left: 276px;
    width: 622px;
    height: 356px;
    overflow: hidden;
  }
  .card--front { top: 175px; background: var(--card-white); }
  .card--back { top: 643px; background: var(--navy); }

  .side-bar {
    position: absolute;
    top: 93px;
    width: 34px;
    height: 170px;
  }
  .side-bar--left { left: 0; }
  .side-bar--right { right: 0; }
  .card--front .side-bar { background: var(--navy); }
  .card--back .side-bar { background: var(--light-grey); }

  .brand {
    position: absolute;
    left: 0;
    right: 0;
    top: 100px;
    display: flex;
    flex-direction: column;
    align-items: center;
    color: var(--navy);
    font-family: "Saira Condensed", "Arial Narrow", sans-serif;
    font-weight: 800;
  }
  .brand__mark {
    width: 62px;
    height: 62px;
    border-radius: 50%;
    background: var(--navy);
    margin-bottom: 14px;
  }
  .brand__name {
    text-align: center;
    line-height: 1;
  }
  .brand__line--main { display: block; font-size: 30px; letter-spacing: 0.5px; }
  .brand__line--sub { display: block; font-size: 24px; margin-top: 2px; }

  .contact-list {
    position: absolute;
    left: 166px;
    top: 111px;
    list-style: none;
    color: var(--light-grey);
    font-family: "Noto Sans", "DejaVu Sans", sans-serif;
    font-weight: 400;
  }
  .contact-item {
    display: flex;
    align-items: center;
    height: 40px;
    margin-bottom: 7px;
  }
  .contact-icon {
    width: 40px;
    height: 40px;
    flex: none;
    margin-right: 20px;
  }
  .contact-item--phone .contact-text { font-size: 17px; letter-spacing: 0.4px; }
  .contact-item--email .contact-text { font-size: 12px; letter-spacing: 0.2px; }
  .contact-item--social .contact-text { font-size: 15px; letter-spacing: 0.2px; }
</style>
</head>
<body>
<main class="canvas">

  <section class="card card--front" aria-label="Card front">
    <div class="side-bar side-bar--left"></div>
    <div class="side-bar side-bar--right"></div>
    <div class="brand">
      <div class="brand__mark"></div>
      <p class="brand__name">
        <span class="brand__line--main">RIVERSTONE PAVING</span>
        <span class="brand__line--sub">&amp; EARTHWORKS</span>
      </p>
    </div>
  </section>

  <section class="card card--back" aria-label="Card back">
    <div class="side-bar side-bar--left"></div>
    <div class="side-bar side-bar--right"></div>
    <ul class="contact-list">
      <li class="contact-item contact-item--phone">
        <svg class="contact-icon" viewBox="0 0 40 40" aria-hidden="true">
          <circle cx="20" cy="20" r="20" fill="#cccccc"/>
          <path d="M14 10 l4 -1 l3 6 l-3 2 q2 5 6 8 l2 -3 l6 3 l-1 4 q-2 2 -5 1 q-9 -4 -13 -14 q-1 -4 1 -6z" fill="#003075"/>
        </svg>
        <span class="contact-text">0439268417</span>
      </li>
      <li class="contact-item contact-item--email">
        <svg class="contact-icon" viewBox="0 0 40 40" aria-hidden="true">
          <rect x="0" y="6" width="40" height="28" fill="#cccccc"/>
          <path d="M0 7 L20 20 L40 7" fill="none" stroke="#003075" stroke-width="2.5"/>
        </svg>
        <span class="contact-text">RiverstonePavingEarthworks@mailbrook.net</span>
      </li>
      <li class="contact-item contact-item--social">
        <svg class="contact-icon" viewBox="0 0 40 40" aria-hidden="true">
          <circle cx="20" cy="20" r="20" fill="#cccccc"/>
        </svg>
        <span class="contact-text">RiverstonePavingEarthworks</span>
      </li>
    </ul>
  </section>

</main>
</body>
</html>
```